Harbor Sushi & Steak Dinner Menu

I'm looking for a MENU design with a particular feel. I want to have a base template made that I can then use for future alterations to the menu; ie I can go in and change out different entrees as the menu changes but the template will remain the same. (Ideally it would be in an Apple Pages format.). Also ideally - dinner menu will occupy 2 pages 8.5 x 11. The restaurant's name is Harbor. It is a MODERN steak house that will also feature Sushi, a Raw Bar, Exquisite Cocktails and a sophisticated nightlife crowd. I have attached our LOGO, a secondary logo that we will be featuring throughout the project including on the menu cover (the gold U). Finally - I have attached the content that we would like to see. AGAIN - I REITERATE: High end dining and lounge atmosphere. A couple of restaurants / menus that I love are Morvendel in NYC and Pellucid Steakhouse in Long Island NY. Please do not duplicate - just trying to offer some suggestions.

Requirements
Must have
• A sophisticated and elegant feel without being stuffy or old.

```html
<!DOCTYPE html>
<html lang="en">
<head>
<meta charset="utf-8">
<title>Harbor Sushi &amp; Steak Dinner Menu</title>
<link href="https://fonts.googleapis.com/css2?family=Montserrat:wght@500;700;800&family=Arimo:wght@400;700&display=swap" rel="stylesheet">
<style>
  :root{
    --backdrop:#e6e0d8;
    --page:#151515;
    --page-edge:#1f1f1f;
    --red:#c8323e;
    --red-band:#b92f3b;
    --white:#f2f2f2;
    --muted:#d9d9d9;
  }
  *{box-sizing:border-box;margin:0;padding:0}
  html,body{width:895px;height:1200px;overflow:hidden;background:var(--backdrop)}
  body{position:relative;font-family:"Arimo",Arial,sans-serif;color:var(--white)}
  .page{position:absolute;background:radial-gradient(ellipse at 50% 40%,var(--page-edge),var(--page) 75%);overflow:hidden}
  .page--cover{left:47px;top:100px;width:370px;height:477px}
  .page--sushi{left:444px;top:100px;width:368px;height:477px}
  .page--kitchen{left:59px;top:665px;width:358px;height:464px}
  .page--sides{left:443px;top:665px;width:360px;height:464px}
  .wave{position:absolute;left:0;bottom:0;width:100%;height:52px}

  .brand{font-family:"Montserrat",sans-serif;font-weight:500;color:var(--white);letter-spacing:.18em;display:flex;align-items:center;justify-content:center;gap:.35em}
  .brand__dot{width:.32em;height:.32em;border-radius:50%;background:var(--red)}
  .cover__brand{position:absolute;left:0;right:0;top:180px;font-size:36px}
  .cover__title{position:absolute;left:0;right:0;top:330px;text-align:center;font-family:"Montserrat",sans-serif;font-weight:800;font-size:20px;line-height:1.2;color:var(--white)}
  .cover__rule{position:absolute;left:152px;top:393px;width:66px;height:2px;background:var(--red)}
  .sushi__brand{position:absolute;left:0;right:0;top:50px;font-size:22px}

  .col{position:absolute}
  .divider{position:absolute;width:0;border-left:1px dashed var(--muted)}
  .heading{display:inline-block;border:1px solid var(--red);padding:1px 12px;margin:0 0 6px 0;font-family:"Arimo",Arial,sans-serif;font-size:11.5px;letter-spacing:.02em;color:var(--white);position:relative}
  .heading::before,.heading::after{content:"";position:absolute;top:2px;bottom:2px;width:4px;border:1px solid var(--red);border-width:1px 0}
  .heading::before{left:-5px}.heading::after{right:-5px}
  .heading--sm{font-size:8.5px;padding:1px 7px}
  .item{font-size:6.3px;line-height:1.3;margin-bottom:4px;color:var(--white)}
  .item b,.name{color:var(--red);font-weight:400}
  .gf{color:var(--red)}
  .list{font-size:6.4px;line-height:1.55;font-weight:700;text-transform:uppercase;margin-bottom:8px}
  .list--plain{font-weight:400}
  .section{margin-bottom:9px}
  .note{font-size:6.4px;line-height:1.35;margin-bottom:6px}
  .photo{position:absolute;left:0;top:253px;width:100%;height:211px;background:linear-gradient(180deg,#3b3330 0%,#8a5a3a 30%,#c78a3a 42%,#2a2c3a 58%,#1d35a8 78%,#0c1230 100%)}
</style>
</head>
<body>

<section class="page page--cover">
  <div class="brand cover__brand"><span class="brand__dot"></span>HARBOR</div>
  <h1 class="cover__title">HARBOR SUSHI &amp; STEAK<br>DINNER MENU</h1>
  <div class="cover__rule"></div>
  <svg class="wave" viewBox="0 0 370 52" preserveAspectRatio="none"><path d="M0 52 L0 38 C90 26 160 8 250 12 C300 14 340 22 370 28 L370 52 Z" fill="var(--red-band)"/><path d="M80 33 C150 16 230 6 370 20" stroke="#000" stroke-width="4" fill="none"/></svg>
</section>

<section class="page page--sushi">
  <div class="brand sushi__brand"><span class="brand__dot"></span>HARBOR</div>
  <div class="divider" style="left:178px;top:108px;height:305px"></div>
  <div class="col" style="left:24px;top:108px;width:150px">
    <div class="section">
      <h2 class="heading">SUSHI / SASHIMI</h2>
      <div class="item"><b>TORO</b> - blue fin tuna belly <span class="gf">(GF)</span></div>
      <div class="item" style="margin-bottom:1px"><b>EBI</b> - cooked shrimp <span class="gf">(GF)</span></div>
      <div class="item" style="margin-bottom:1px"><b>HAMACHI</b> - yellowtail <span class="gf">(GF)</span></div>
      <div class="item" style="margin-bottom:1px"><b>UNI</b> - sea urchin <span class="gf">(GF)</span></div>
      <div class="item" style="margin-bottom:1px"><b>HIRAME</b> - fluke <span class="gf">(GF)</span></div>
      <div class="item" style="margin-bottom:1px"><b>UNAGI</b> - fresh water eel <span class="gf">(GF)</span></div>
      <div class="item" style="margin-bottom:1px"><b>SAKE</b> - salmon <span class="gf">(GF)</span></div>
      <div class="item" style="margin-bottom:1px"><b>MADAI</b> - red snapper <span class="gf">(GF)</span></div>
      <div class="item"><b>MAGURO</b> - tuna <span class="gf">(GF)</span></div>
    </div>
    <div class="section">
      <h2 class="heading">SUSHI PLATTERS</h2>
      <div class="item"><b>SMALL</b> - Five Pieces assorted sushi, nine pieces sashimi, spicy tuna roll <span class="gf">(GF)</span></div>
      <div class="item"><b>LARGE</b> - Eight Pieces assorted sushi, eighteen pieces of sashimi, alaskan roll, rainbow roll <span class="gf">(GF)</span></div>
    </div>
    <div class="section">
      <h2 class="heading">CLASSIC ROLLS</h2>
      <div class="item"><b>YELLOWTAIL</b>- inside out roll with scallions <span class="gf">(GF)</span></div>
      <div class="item"><b>SPICY TUNA OR SALMON OR YELLOWTAIL</b> - spicy mayo <span class="gf">(GF)</span></div>
      <div class="item"><b>CALIFORNIA</b> - crab meat, cucumber and avocado <span class="gf">(GF)</span></div>
      <div class="item"><b>VEGETABLE</b> - avocado, cucumber, asparagus and pickled reddish <span class="gf">(GF)</span></div>
    </div>
  </div>
  <div class="col" style="left:197px;top:106px;width:150px">
    <div class="section">
      <div class="item"><b>SPIDER</b> - soft shell crab and avocado with eel sauce</div>
      <div class="item"><b>SHRIMP TEMPURA</b> - deep fried tempura shrimp and eel sauce</div>
      <div class="item"><b>ALASKAN</b> - salmon and avocado <span class="gf">(GF)</span></div>
    </div>
    <div class="section">
      <h2 class="heading">SPECIAL ROLLS</h2>
      <div class="item"><b>THE HARBOR</b> - tuna, salmon, yellowtail, avocado, spicy mayo, soy bean paper</div>
      <div class="item"><b>KING CRAB RAINBOW</b> - king crab, avocado, cucumbers, assorted fish on top</div>
      <div class="item"><b>EMPRESS</b> - Shrimp tempura, spicy tuna on top, eel sauce, spicy mayo</div>
      <div class="item"><b>SPICY GIRL</b> - Spicy crunchy crab meat, cucumber, shrimp on top</div>
      <div class="item"><b>DRAGON</b> - Eel, cucumber, avocado, and tobiko on top, eel sauce</div>
      <div class="item"><b>YUMMY</b> - spicy crunchy salmon, avocado, mango and salmon on top</div>
      <div class="item"><b>NO. 9</b> - Shrimp Tempura, avocado, kani, spicy mayo, tobiko</div>
      <div class="item"><b>SUNRISE ROLL</b> - spicy crunchy tuna and avocado, spicy crunchy salmon on top</div>
    </div>
    <div class="section">
      <h2 class="heading">SEAFOOD RAW BAR</h2>
      <div class="list">Lobster cocktail<br>Shrimp cocktail<br>Clams on the half shell<br>Oysters on the half shell<br>Colossal crab cocktail</div>
    </div>
  </div>
  <svg class="wave" viewBox="0 0 368 52" preserveAspectRatio="none"><path d="M0 52 L0 20 C60 34 120 36 200 26 C270 16 330 16 368 26 L368 52 Z" fill="var(--red-band)"/><path d="M0 18 C80 30 150 32 230 20 C290 12 340 14 368 22" stroke="#000" stroke-width="4" fill="none"/></svg>
</section>

<section class="page page--kitchen">
  <div class="divider" style="left:176px;top:32px;height:362px"></div>
  <div class="col" style="left:30px;top:32px;width:142px">
    <div class="section">
      <h2 class="heading heading--sm">RAW BAR PLATE FOR ONE:</h2>
      <div class="note">Two Shrimp, Half of a One Pound Lobster, Two Clams, One East Coast Oyster, One West Coast Oyster</div>
    </div>
    <div class="section">
      <h2 class="heading heading--sm">SEAFOOD PLATTERS <span class="gf">(GF)</span></h2>
      <div class="note">Shrimp, Oysters, Clams, Lobster and Crab<br>LARGE OR COLOSSAL</div>
    </div>
    <div class="section">
      <h2 class="heading heading--sm">APPS</h2>
      <div class="item">BAO Bun; hoisin bbq pancetta cut pork loin, crispy onions, micro mint</div>
      <div class="item"><span class="name">Five Spice Crispy Popcorn Crusted Prawns (2)</span><br>classic burre blanc</div>
      <div class="item"><span class="name">Crispy Wonton Napoleon</span><br>cucumber gallete, ahi tuna, jumbo lump crab meat, wasabi aioli, shoestring wontons</div>
      <div class="item"><span class="name">PEI Mussels</span><br>PEI Mussels; charred artichoke hearts, blistered heirloom tomatoes, garlic white wine broth</div>
      <div class="item"><span class="name">New Zealand or Domestic Small Eye Lamb Chop (1)</span><br>crispy porcini risotto cake</div>
    </div>
    <div class="section">
      <h2 class="heading heading--sm">SALADS</h2>
      <div class="item"><span class="name">Classic Wedge</span><br>bleu cheese, bacon lardons, heirloom tomatoes</div>
      <div class="item"><span class="name">Mixed Baby Greens</span><br>heirloom tomatoes, cucumber, red onion, dijon vinaigrette</div>
      <div class="item"><span class="name">Tabulleh</span><br>buckwheat grain, fresh mint, tomato concasse, cucumber, parsley, fresh squeezed lemon, EVOO., salt and pepper<br><span class="name">Tomato Mozzarella Salad / Burratta</span></div>
    </div>
  </div>
  <div class="col" style="left:189px;top:30px;width:150px">
    <div class="section">
      <div class="item"><span class="name">Spinach Salad</span><br>green apple, feta, currants, with per-simmons vinaigrette</div>
      <div class="item"><span class="name">Kale Caesar</span><br>homemade cacio e'peppe dressing, pecorino and parmesan cheese, toasted croutons.</div>
    </div>
    <div class="section">
      <h2 class="heading">ENTREES</h2>
      <div class="item"><span class="name">Pan Roasted Miso Glazed Black Cod</span><br>green tea noodle stir fry; Napa cabbage, carrot, Japanese eggplant</div>
      <div class="item"><span class="name">Pan Seared Striped Bass;</span><br>lobster succotash in a tomato saffron broth</div>
      <div class="item"><span class="name">E.V.O.O. Salted / Grilled Swordfish;</span><br>un dried tomato, olive and caper tapenade, over basmati rice</div>
      <div class="item"><span class="name">Grilled Half Chicken;</span><br>sun dried tomato and basil Israeli cous-cous, pan au jus</div>
      <div class="item"><span class="name">Roasted Fresh Caviatelle Ratatoille</span><br>vegetable broth</div>
      <div class="item"><span class="name">Lobster Cartoccio;</span><br>shrimp, mussels, clams, fresh herb tomato broth, tossed with bucatini</div>
      <div class="item">Charred Artichoke Hearts, heirloom tomatoes, caper berries, spring onions, fresh basil, white wine reduction over forbidden rice (gf)</div>
      <div class="item"><span class="name">Mediterranean Grilled Veggie Plate</span><br>Artichoke hearts, Japanese eggplant, green &amp; white asparagus, seared heirloom tomatoes, roasted baby carrots, cauliflower rice, evoo &amp; fig drizzle (gf)</div>
    </div>
    <div class="section">
      <h2 class="heading heading--sm" style="font-size:9.5px">USDA PRIME STEAKS (gf)</h2>
      <div class="list" style="line-height:1.45">10 oz Filet<br>14 or 16 oz New York Strip<br>24 oz Boneless Ribeye<br>36 oz Bone in Rib Eye<br>36 oz Bone in Rib Eye</div>
    </div>
  </div>
  <svg class="wave" viewBox="0 0 358 52" preserveAspectRatio="none"><path d="M0 52 L0 46 C90 40 180 26 260 16 C300 12 335 14 358 18 L358 52 Z" fill="var(--red-band)"/><path d="M90 42 C170 30 250 12 358 10" stroke="#000" stroke-width="4" fill="none"/></svg>
</section>

<section class="page page--sides">
  <div class="divider" style="left:178px;top:62px;height:137px"></div>
  <div class="col" style="left:29px;top:60px;width:145px">
    <h2 class="heading heading--sm">SAUCES</h2>
    <div class="list list--plain">Cabernet Demi Glaz<br>Gorganzola Brulle Cream<br>Truffled Wild Mushroom Ragum<br>Horseradish Cream<br>House Steak Sauce</div>
    <div style="font-size:8px;margin-top:4px">DESSERTS</div>
    <div class="list list--plain">T.B.D. - Separate Menu</div>
  </div>
  <div class="col" style="left:195px;top:62px;width:150px">
    <h2 class="heading heading--sm">SIDES</h2>
    <div class="list list--plain" style="line-height:1.6">Mashed Idaho Potatoes<br>Bacon, Sweet Corn, Caramelized Vidalia Onion Fingerling Potatoes<br>Roasted Peanut Potatoes<br>Creamed Spinach<br>Sautéed Spinach<br>Grilled Asparagus<br>French Beans<br>Israeli Cous Cous<br>Sweet Potato Steak Fries<br>Corn Skillet</div>
  </div>
  <div class="photo" role="img" aria-label="Photo of the lounge bar with blue-lit counter, bar stools and a colourful wall mural"></div>
  <svg class="wave" viewBox="0 0 360 52" preserveAspectRatio="none"><path d="M0 52 L0 30 C70 34 140 38 210 32 C280 24 330 22 360 26 L360 52 Z" fill="var(--red-band)"/><path d="M0 28 C90 34 170 34 240 24 C300 16 340 18 360 20" stroke="#000" stroke-width="4" fill="none"/><path d="M0 0 L360 0 L360 22 C330 16 280 18 230 22 C160 30 80 30 0 24 Z" fill="none"/></svg>
</section>

</body>
</html>
```